Postcard Design

The Willow Bend Courier ~ Your #1 Newspaper since 1971

I am trying to reach new clients with our special of
Receive 1 month free with a year contract.

The Willow Bend Courier is a monthly newspaper that readers cherish like a magazine waiting for the next one to be published. I have had several advertisers since the first paper in 1971. My mom was the prior owner and she loved roosters, hence the rooster in the logo.
Updates

Please add the following:

Your # 1 Newspaper 

Serving Ocean County since 1971

1 Month FREE with 1 Year Contract

Instead of your #1 Newspaper...please put

The areas best place to see what's happening locally.

Target Market(s)

professionals, restaurants, etc.

Colors
33b7a4
85cae6
33a6d7

Requirements
Must have
• P.O. Box 457, Willow Bend, NJ 08314
Email: info@willowbendcourier.example
609.555.0182
www.willowbendcourier.example
Nice to have
• Typical savings up to $300.

```html
<!DOCTYPE html>
<html lang="en">
<head>
<meta charset="utf-8">
<title>The Willow Bend Courier — Postcard</title>
<link href="https://fonts.googleapis.com/css2?family=Tinos:ital,wght@0,700;1,700&family=Arimo:wght@700&family=Alegreya:ital,wght@1,700&display=swap" rel="stylesheet">
<style>
  :root {
    --frame-blue: #1a92d4;
    --curl-blue: #1d8fd3;
    --sky: #85cae6;
    --teal: #33b7a4;
    --rule-grey: #5a5a5a;
    --logo-grey: #666a6d;
    --headline-red: #e3171d;
    --body-navy: #2b2a8c;
    --ink: #111;
    --white: #fff;
  }
  html, body {
    margin: 0;
    padding: 0;
    width: 1200px;
    height: 930px;
    overflow: hidden;
    background: var(--white);
  }
  .postcard {
    position: relative;
    width: 1200px;
    height: 930px;
    background: var(--white);
  }
  .frame {
    position: absolute;
    left: 36px; top: 36px;
    width: 1128px; height: 854px;
    background: var(--frame-blue);
  }
  .frame-inner {
    position: absolute;
    left: 4px; top: 4px; right: 4px; bottom: 4px;
    background: var(--white);
    overflow: hidden;
  }
  .side-glow {
    position: absolute;
    left: 0; top: 0; bottom: 0;
    width: 66px;
    background: linear-gradient(90deg, var(--frame-blue) 0%, #7cc3ea 45%, rgba(255,255,255,0) 100%);
  }
  .masthead {
    position: absolute;
    left: 57px; top: 46px;
    width: 1082px; height: 198px;
    border: 2px solid var(--rule-grey);
    display: flex;
    align-items: center;
    justify-content: center;
    gap: 26px;
  }
  .masthead-mark {
    width: 112px; height: 112px;
    border-radius: 50%;
    background: var(--teal);
  }
  .masthead-name {
    font-family: "Tinos", "Times New Roman", serif;
    font-weight: 700;
    font-size: 64px;
    color: var(--logo-grey);
    letter-spacing: 1px;
    margin: 0;
  }
  .tagline-band {
    position: absolute;
    left: 57px; top: 250px;
    width: 1086px; height: 50px;
    background: linear-gradient(90deg, var(--teal) 0%, #bfe8e1 22%, #ffffff 45%, #ffffff 60%, #bfe8e1 80%, var(--teal) 100%);
    display: flex;
    align-items: center;
    justify-content: center;
    font-family: "Arimo", Arial, sans-serif;
    font-weight: 700;
    font-size: 27px;
    letter-spacing: 0.5px;
    color: var(--ink);
  }
  .content {
    position: absolute;
    left: 57px; top: 304px;
    width: 1082px; height: 564px;
    border: 2px solid var(--rule-grey);
  }
  .ornament {
    position: absolute;
    left: 62px; top: 386px;
    width: 470px; height: 474px;
    background: radial-gradient(ellipse at 30% 70%, rgba(232,45,130,0.55) 0%, rgba(246,166,35,0.45) 35%, rgba(40,150,210,0.25) 60%, rgba(255,255,255,0) 75%);
  }
  .headline {
    position: absolute;
    left: 230px; top: 336px;
    width: 740px;
    text-align: center;
    margin: 0;
    font-family: "Tinos", "Times New Roman", serif;
    font-style: italic;
    font-weight: 700;
    font-size: 46px;
    line-height: 54px;
    color: var(--headline-red);
  }
  .headline span { display: block; }
  .pitch {
    position: absolute;
    left: 290px; top: 486px;
    width: 600px;
    margin: 0;
    text-align: center;
    font-family: "Alegreya", Georgia, serif;
    font-style: italic;
    font-weight: 700;
    font-size: 41px;
    line-height: 55px;
    color: var(--body-navy);
  }
  .pitch span { display: block; }
  .contact {
    position: absolute;
    left: 330px; top: 730px;
    width: 520px;
    margin: 0;
    text-align: center;
    font-family: "Arimo", Arial, sans-serif;
    font-weight: 700;
    font-size: 19px;
    line-height: 30px;
    color: var(--body-navy);
    font-style: normal;
  }
  .contact span { display: block; }
  .curl {
    position: absolute;
    left: 0; top: 0;
    width: 1200px; height: 930px;
  }
  .offer {
    position: absolute;
    left: 895px; top: 700px;
    width: 260px;
    text-align: center;
    transform: rotate(-45deg);
    font-family: "Tinos", "Times New Roman", serif;
    font-weight: 700;
    color: var(--ink);
    line-height: 1.05;
  }
  .offer-main { display: block; font-size: 38px; }
  .offer-sub { display: block; font-size: 26px; }
</style>
</head>
<body>
<div class="postcard">
  <div class="frame"><div class="frame-inner"><div class="side-glow"></div></div></div>

  <header class="masthead">
    <div class="masthead-mark"></div>
    <h1 class="masthead-name">The Willow Bend Courier</h1>
  </header>

  <div class="tagline-band">SERVING OCEAN COUNTY&nbsp; SINCE 1971</div>

  <section class="content"></section>

  <div class="ornament" role="img" aria-label="Colourful paisley swirl ornament in pink, orange, blue and brown"></div>

  <h2 class="headline"><span>The Area’s Best Place to See</span><span>What’s Happening Locally</span></h2>

  <p class="pitch"><span>A “Magazine” that</span><span>readers cherish throughout the</span><span>month with the anticipation</span><span>of the next one.</span></p>

  <address class="contact">
    <span>P.O. Box 457, Willow Bend, NJ 08314 &nbsp;·&nbsp; 609.555.0182</span>
    <span>info@willowbendcourier.example</span>
    <span>www.willowbendcourier.example</span>
  </address>

  <svg class="curl" viewBox="0 0 1200 930" aria-hidden="true">
    <defs>
      <linearGradient id="reveal" x1="0" y1="0" x2="1" y2="1">
        <stop offset="0" stop-color="#ffffff"/>
        <stop offset="0.45" stop-color="#cfe9f6"/>
        <stop offset="1" stop-color="#85cae6"/>
      </linearGradient>
    </defs>
    <path d="M1147 548 L1147 884 L700 884 C900 800 1050 660 1147 548 Z" fill="url(#reveal)"/>
    <path d="M966 503 C992 620 905 800 700 884 C900 800 1050 660 1147 548 C1060 580 992 560 966 503 Z" fill="var(--curl-blue)"/>
  </svg>

  <div class="offer">
    <span class="offer-main">1 Month FREE</span>
    <span class="offer-sub">with 1 Year</span>
    <span class="offer-sub">Contract</span>
  </div>
</div>
</body>
</html>
```